Tidal Bloomz - Sovereign rings, pendants & custom cultural pieces

I need a website that attracts customers knowing that I am as per detailed below Everyone deserves a special piece of treasure. At Tidal Bloomz we provide you with unique, high-quality and affordable Sovereign rings, pendants & custom cultural pieces.
Feel free to check my Picorama page to get idea's @tidal.bloomz
I want people to see the Items I have available & know that my prices are very competitive. I want people to be able to Shop/Purchase items via site. I would like to have Tidal Bloomz Friendlio, Picorama & Swapzo Icon/tabs on site so customers can link a at click of the mouse.

(My Apologies to you all, This is all overwhelming & new to myself & I appreciate your efforts & work detail)
Updates

Apologies, have had family loss to deal with

Still dealing with loss of family member

Still Dealing with Family member passing

As previously, still getting through the loss of a family member

As per previous extensions, re adjusting to life after loss of family member

As per previously still recovering from loss of family member

As previously expressed

Haven’t recovered from family loss

I am still getting life back together

Target Market(s)

Jewellery, Wedding, Gifts, Pacific people, Persons 18 - 65yrs, New Zealand & Australian

Industry/Entity Type

Jewelry

Contact Information for Business Card

Tidal Bloomz
Reko Tumanu
Friendlio @tidalbloomz
Picorama @tidal.bloomz
Phone Number 021 07351942
Website www.tidalbloomz-example.co.nz
Auckland
New Zealand

Number of Pages Required

5+ page

Font styles to use
Sans Serif

Colors
474747
1b1b1b
000000
cfcfcf
fbed22
ffc214
ffffff

Requirements
Must have
• Using Black / Gold Tidal Bloomz logo with crown, has been attached to Web design.
• Reko Tumanu
• Friendlio Tidal Bloomz
• Picorama @tidal.bloomz
• Swapzo Tidal Bloomz
• Phone Number 021 07351942
• Website www.tidalbloomz-example.co.nz
Nice to have
• Thinking black card with the Tidal Bloomz Gold logo
• Lines on back of card for Customer Quoted Prices

```html
<!DOCTYPE html>
<html lang="en">
<head>
<meta charset="utf-8">
<title>Tidal Bloomz — Rings, Pendants &amp; Cultural Pieces</title>
<link href="https://fonts.googleapis.com/css2?family=Montserrat:wght@300;400;500;600;700&family=Raleway:wght@300;400;500&display=swap" rel="stylesheet">
<style>
:root{
  --black:#000000;
  --ink:#1b1b1b;
  --graphite:#474747;
  --silver:#cfcfcf;
  --lemon:#fbed22;
  --gold:#ffc214;
  --white:#ffffff;
  --rock-a:#2a2a2a;
  --rock-b:#0d0d0d;
}
*{box-sizing:border-box;margin:0;padding:0}
html,body{width:1200px;height:3756px;overflow:hidden}
body{background:var(--black);color:var(--white);font-family:"Montserrat",Arial,sans-serif;position:relative}
.section{position:absolute;left:0;width:1200px}
.heading{font-family:"Raleway",Arial,sans-serif;font-weight:400;font-size:30px;letter-spacing:1px;text-align:center;text-transform:uppercase}
.btn{display:inline-block;border:1px solid var(--white);color:var(--white);font-size:12px;letter-spacing:1px;text-transform:uppercase;text-align:center;line-height:40px;height:42px;padding:0 28px;background:transparent}
.rock{background:radial-gradient(ellipse at 30% 40%,var(--rock-a),var(--rock-b) 70%)}

/* header */
.site-header{top:0;height:120px;background:var(--black);display:flex;align-items:center;justify-content:space-between;padding:0 40px}
.menu-icon span{display:block;width:24px;height:3px;background:var(--white);margin:4px 0}
.brand{position:absolute;left:50%;top:18px;transform:translateX(-50%);text-align:center}
.brand-mark{width:34px;height:34px;background:var(--gold);margin:0 auto 8px}
.brand-name{font-family:"Montserrat",sans-serif;font-weight:600;font-size:15px;letter-spacing:2px;color:var(--gold);text-transform:uppercase;white-space:nowrap}
.header-icons{display:flex;gap:22px}

/* hero */
.hero{top:120px;height:560px}
.hero-photo{position:absolute;left:520px;top:60px;width:620px;height:420px;border-radius:50%;background:radial-gradient(ellipse,#c9c3b5,#8a7254 45%,rgba(20,20,20,0) 72%)}
.hero-copy{position:absolute;left:100px;top:210px;width:420px;height:170px;border:1px solid var(--silver);padding:22px 20px}
.hero-copy .kicker{font-family:"Raleway",sans-serif;font-size:28px;letter-spacing:3px;font-weight:300}
.hero-copy .title{font-size:40px;font-weight:700;color:var(--gold);letter-spacing:2px;line-height:1.05;white-space:nowrap}
.hero-copy .sub{font-family:"Raleway",sans-serif;font-size:28px;letter-spacing:3px;font-weight:300;color:var(--silver)}
.hero-copy .btn{position:absolute;left:250px;bottom:-20px;background:var(--black);height:36px;line-height:34px;padding:0 18px;font-size:11px}

/* product grids */
.products{background:var(--black)}
.featured{top:680px;height:720px}
.best{top:1800px;height:640px}
.tabs{display:flex;justify-content:center;gap:26px;font-size:12px;text-transform:uppercase;margin-top:22px;color:var(--silver)}
.tabs .active{color:var(--white)}
.grid{position:absolute;left:112px;width:976px;display:flex;gap:24px}
.card{width:226px;text-align:center}
.card-photo{width:226px;height:240px;background:radial-gradient(circle,#b7a88e,#5e5648 70%,#2c2c2c)}
.card-photo.rose{background:radial-gradient(circle,#d8a480,#8a5a3c 65%,#3a3a3a)}
.card-photo.silver{background:radial-gradient(circle,#d6d6d2,#7c7c78 65%,#3a3a3a)}
.card-name{font-size:16px;text-transform:uppercase;margin-top:26px}
.card-price{font-size:15px;margin-top:8px;color:var(--silver)}
.card .btn{margin-top:16px;width:150px;padding:0}
.arrow{position:absolute;font-size:40px;color:var(--white);font-family:"Raleway",sans-serif}
.more{position:absolute;left:525px;width:150px;padding:0}

/* offer */
.offer{top:1400px;height:400px;text-align:center}
.offer-photo{position:absolute;top:80px;width:300px;height:220px;border-radius:50%;background:radial-gradient(ellipse,#b48a64,#5a4432 55%,rgba(0,0,0,0) 72%)}
.offer-copy{position:absolute;left:0;width:1200px;top:100px}
.offer-copy .kicker{font-family:"Raleway",sans-serif;font-size:22px;letter-spacing:2px;color:var(--silver)}
.offer-copy .big{font-size:48px;font-weight:700;color:var(--gold);margin-top:4px}
.offer-copy .small{font-size:34px;font-weight:500;color:var(--lemon)}
.offer-copy .btn{margin-top:14px;height:36px;line-height:34px;font-size:11px}

/* testimonial */
.testimonial{top:2440px;height:440px;text-align:center}
.quote{position:absolute;left:320px;width:560px;top:150px;font-size:13px;line-height:1.5;color:var(--silver)}
.quote-mark{position:absolute;top:136px;font-family:"Raleway",sans-serif;font-size:52px;font-weight:500}
.client{position:absolute;top:230px;width:1200px;font-size:28px;font-weight:500;color:var(--gold);letter-spacing:1px}
.stars{position:absolute;top:280px;width:1200px;color:var(--gold);font-size:18px;letter-spacing:3px}
.dots{position:absolute;top:318px;width:1200px;display:flex;justify-content:center;gap:10px}
.dots i{width:8px;height:8px;border-radius:50%;background:var(--graphite)}
.dots i.on{background:var(--white)}

/* contact */
.contact{top:2880px;height:460px;background:var(--black)}
.form{position:absolute;left:356px;width:524px;top:156px}
.field{border:1px solid var(--silver);height:44px;margin-bottom:14px;font-size:13px;color:var(--silver);padding:12px 16px;background:var(--black)}
.field.area{height:80px}
.submit{height:44px;background:var(--gold);color:var(--black);font-size:13px;text-transform:uppercase;text-align:center;line-height:44px}

/* footer */
.site-footer{top:3340px;height:340px;background:var(--ink)}
.foot-col{position:absolute;top:70px}
.foot-col h4{font-size:15px;font-weight:500;margin-bottom:6px}
.foot-col h4::after{content:"";display:block;width:30px;height:2px;background:var(--white);margin-top:6px}
.foot-brand{left:120px;top:60px;width:200px}
.foot-brand .brand-mark{margin:0 0 6px 18px}
.foot-brand .brand-name{font-size:12px}
.foot-about{font-size:12px;line-height:1.45;color:var(--silver);margin-top:14px}
.payments{display:flex;gap:8px;margin-top:34px}
.payments span{width:34px;height:22px;background:var(--graphite);border-radius:3px}
.links{left:416px}
.links li{list-style:none;font-size:12px;line-height:22px;color:var(--silver)}
.links li::before{content:"›";margin-right:8px}
.tags{left:572px}
.tag-grid{display:grid;grid-template-columns:repeat(3,64px);gap:10px;margin-top:14px}
.tag-grid span{border:1px solid var(--silver);height:28px;line-height:26px;font-size:11px;text-align:center;color:var(--silver)}
.quick{left:816px;width:270px}
.quick-row{display:flex;gap:14px;margin-top:16px}
.quick-row div,.quick-msg{border-bottom:1px solid var(--graphite);font-size:11px;color:var(--silver);padding:6px 0;flex:1}
.quick-msg{margin-top:10px;height:48px}
.quick-send{margin-top:18px;background:var(--gold);color:var(--black);height:32px;line-height:32px;text-align:center;font-size:12px}
.bottom-bar{top:3680px;height:76px;background:var(--black);display:flex;align-items:center;justify-content:space-between;padding:0 112px;font-size:13px;color:var(--silver)}
.social{display:flex;gap:18px}
.social span{width:18px;height:18px;background:var(--silver)}
</style>
</head>
<body>

<header class="section site-header">
  <div class="menu-icon"><span></span><span></span><span></span></div>
  <div class="brand"><div class="brand-mark"></div><div class="brand-name">Tidal Bloomz</div></div>
  <div class="header-icons">
    <svg width="18" height="18" viewBox="0 0 18 18" fill="none" stroke="#fff" stroke-width="2"><circle cx="7.5" cy="7.5" r="5.5"/><path d="M12 12l5 5"/></svg>
    <svg width="18" height="18" viewBox="0 0 18 18" fill="none" stroke="#fff" stroke-width="2"><circle cx="9" cy="6" r="4"/><path d="M2 17c1-4 4-5 7-5s6 1 7 5"/></svg>
    <svg width="18" height="18" viewBox="0 0 18 18" fill="none" stroke="#fff" stroke-width="2"><path d="M9 16S2 11 2 6a3.5 3.5 0 0 1 7-1 3.5 3.5 0 0 1 7 1c0 5-7 10-7 10z"/></svg>
    <svg width="18" height="18" viewBox="0 0 18 18" fill="none" stroke="#fff" stroke-width="2"><path d="M3 6h12l-1 10H4z"/><path d="M6 6a3 3 0 0 1 6 0"/></svg>
  </div>
</header>

<section class="section hero rock">
  <div class="hero-photo" role="img" aria-label="Silver and rose gold Tongan mint coin rings on dark stone"></div>
  <div class="hero-copy">
    <div class="kicker">STERLING</div>
    <div class="title">SILVER TONGAN</div>
    <div class="sub">MINT RING</div>
    <span class="btn">Shop Now</span>
  </div>
</section>

<section class="section products featured">
  <h2 class="heading" style="margin-top:66px">Feature Products</h2>
  <div class="tabs"><span class="active">All</span><span>Latest</span><span>Best Seller</span><span>Discounted</span><span>Other</span></div>
  <span class="arrow" style="left:30px;top:230px">‹</span>
  <span class="arrow" style="left:1152px;top:230px">›</span>
  <div class="grid" style="top:192px">
    <div class="card"><div class="card-photo silver" role="img" aria-label="Silver coin signet ring"></div><div class="card-name">Product Name</div><div class="card-price">$ 500.0</div><span class="btn">Shop Now</span></div>
    <div class="card"><div class="card-photo silver" role="img" aria-label="Silver crest ring"></div><div class="card-name">Product Name</div><div class="card-price">$ 500.0</div><span class="btn">Shop Now</span></div>
    <div class="card"><div class="card-photo" role="img" aria-label="Coin pendant"></div><div class="card-name">Product Name</div><div class="card-price">$ 500.0</div><span class="btn">Shop Now</span></div>
    <div class="card"><div class="card-photo rose" role="img" aria-label="Rose gold coin ring"></div><div class="card-name">Product Name</div><div class="card-price">$ 500.0</div><span class="btn">Shop Now</span></div>
  </div>
  <span class="btn more" style="top:636px">Shows More</span>
</section>

<section class="section offer rock">
  <div class="offer-photo" style="left:40px" role="img" aria-label="Pair of gold coin rings"></div>
  <div class="offer-photo" style="left:860px" role="img" aria-label="Pair of gold signet rings"></div>
  <div class="offer-copy">
    <div class="kicker">DISCOUNT OFFER</div>
    <div class="big">SAVE 40% OFF</div>
    <div class="small">ON YOUR 1st ORDER</div>
    <span class="btn">Shop Now</span>
  </div>
</section>

<section class="section products best">
  <h2 class="heading" style="margin-top:64px">Best Seller</h2>
  <span class="arrow" style="left:30px;top:180px">‹</span>
  <span class="arrow" style="left:1152px;top:180px">›</span>
  <div class="grid" style="top:128px">
    <div class="card"><div class="card-photo rose" role="img" aria-label="Gold coin stud earrings"></div><div class="card-name">Product Name</div><span class="btn">Shop Now</span></div>
    <div class="card"><div class="card-photo rose" role="img" aria-label="Gold coin bracelet"></div><div class="card-name">Product Name</div><span class="btn">Shop Now</span></div>
    <div class="card"><div class="card-photo silver" role="img" aria-label="Silver coin ring"></div><div class="card-name">Product Name</div><span class="btn">Shop Now</span></div>
    <div class="card"><div class="card-photo rose" role="img" aria-label="Rose gold coin ring"></div><div class="card-name">Product Name</div><span class="btn">Shop Now</span></div>
  </div>
  <span class="btn more" style="top:544px">Shows More</span>
</section>

<section class="section testimonial rock">
  <h2 class="heading" style="padding-top:92px">Our Clients Say's</h2>
  <span class="quote-mark" style="left:280px">“</span>
  <p class="quote">Lorem ipsum is simply dummy text of the printing and typesetting industry. Lorem ipsum has been the industry standard dummy text ever since the 1500s.</p>
  <span class="quote-mark" style="left:896px">”</span>
  <div class="client">MARA LENTON</div>
  <div class="stars">★★★★★</div>
  <div class="dots"><i></i><i class="on"></i><i></i></div>
  <span class="btn" style="position:absolute;left:525px;top:352px;width:150px;padding:0">Shows More</span>
</section>

<section class="section contact">
  <h2 class="heading" style="margin-top:78px">Contact Us</h2>
  <div class="form">
    <div class="field">Your Name</div>
    <div class="field">Email Address</div>
    <div class="field area">Message</div>
    <div class="submit">Submit Now</div>
  </div>
</section>

<footer class="section site-footer">
  <div class="foot-col foot-brand">
    <div class="brand-mark"></div>
    <div class="brand-name">Tidal Bloomz</div>
    <p class="foot-about">Lorem ipsum is simply dummy text of the printing and typesetting text of the printing and typesetting in the industry. Read More...</p>
    <div class="payments"><span></span><span></span><span></span><span></span><span></span></div>
  </div>
  <div class="foot-col links">
    <h4>Quick Link</h4>
    <ul><li>Home</li><li>About us</li><li>Feature Product</li><li>Testimonials</li><li>Blogs</li><li>Contact Us</li></ul>
  </div>
  <div class="foot-col tags">
    <h4>Popular Tags</h4>
    <div class="tag-grid"><span>Ring</span><span>Jewelry</span><span>Lady</span><span>Women</span><span>Men</span><span>Specials</span><span>Fashion</span><span>Bracelet</span><span>Offers</span><span>Men</span><span>Hot</span></div>
  </div>
  <div class="foot-col quick">
    <h4>Quick Contact</h4>
    <div class="quick-row"><div>Name</div><div>Phone</div></div>
    <div class="quick-msg">Message</div>
    <div class="quick-send">Send</div>
  </div>
</footer>

<div class="section bottom-bar">
  <span>© Copyright 2018 Tidal Bloomz. All Rights Reserved.</span>
  <div class="social"><span></span><span></span><span></span><span></span><span></span></div>
</div>

</body>
</html>
```